Bref créative
Biz Card for a Professional Organizer
Dana Kowalt
Cutting-Edge
Room Clearing Maestro
Serving the Bay Area
info@42plumova.com
www.42plumova.com
I'd like a clean design, possibly going vertical instead of the traditional horizontal-UNLESS it is just going to look better going horizontal.
I'm open to suggestions here. I also have black and white versions of my logo if that would work well here...
black version of logo
reverse version of logo
color version

```html
<!DOCTYPE html>
<html lang="en">
<head>
<meta charset="utf-8">
<title>42 Plumova – Business Card</title>
<link rel="stylesheet" href="https://fonts.googleapis.com/css2?family=Open+Sans:wght@400;600;700&display=swap">
<style>
  :root {
    --backdrop: #8d8d8d;
    --card-black: #050505;
    --card-white: #ffffff;
    --brand-blue: #4b8fa8;
    --band-slate: #243640;
    --text-dark: #2b2b2b;
    --text-muted: #6b6b6b;
  }
  * { margin: 0; padding: 0; box-sizing: border-box; }
  html, body {
    width: 1200px;
    height: 1099px;
    overflow: hidden;
    background: var(--backdrop);
    font-family: "Open Sans", Arial, sans-serif;
  }
  .card {
    position: absolute;
    width: 405px;
    border-radius: 24px;
    overflow: hidden;
    background: var(--card-black);
  }
  .card--front { left: 170px; top: 92px; height: 709px; }
  .card--back  { left: 613px; top: 316px; height: 705px; }

  .brand-name {
    position: absolute;
    left: 0; right: 0;
    text-align: center;
    font-weight: 600;
    font-size: 40px;
    line-height: 1;
    color: var(--brand-blue);
  }
  .card--front .brand-name { top: 190px; }
  .card--back .brand-name { top: 362px; }

  .person {
    position: absolute;
    left: 0; right: 0;
    top: 386px;
    text-align: center;
  }
  .person__name {
    font-weight: 700;
    font-size: 24px;
    line-height: 30px;
    color: var(--brand-blue);
  }
  .person__title {
    font-size: 12px;
    line-height: 16px;
    color: var(--brand-blue);
    opacity: 0.8;
  }

  .divider { position: absolute; left: 0; right: 0; top: 466px; }
  .divider__line { height: 4px; background: var(--brand-blue); }
  .divider__band { height: 18px; background: var(--band-slate); margin-top: 3px; }

  .contact {
    position: absolute;
    left: 0; right: 0;
    top: 492px;
    bottom: 0;
    background: var(--card-white);
  }
  .contact__details {
    position: absolute;
    left: 128px;
    top: 48px;
    font-size: 14px;
    line-height: 22px;
    color: var(--text-dark);
  }
  .contact__details b { font-weight: 700; }
  .contact__web {
    position: absolute;
    left: 40px; right: 40px;
    top: 150px;
    text-align: center;
    font-size: 14px;
    letter-spacing: 3px;
    color: var(--text-muted);
    padding-bottom: 4px;
    border-bottom: 2px solid var(--brand-blue);
  }
</style>
</head>
<body>
  <section class="card card--front" aria-label="Card front">
    <p class="brand-name">42 Plumova</p>
    <div class="person">
      <p class="person__name">Dana Kowalt</p>
      <p class="person__title">Room Clearing Maestro</p>
    </div>
    <div class="divider">
      <div class="divider__line"></div>
      <div class="divider__band"></div>
    </div>
    <div class="contact">
      <div class="contact__details">
        <p>Serving the Bay Area</p>
        <p><b>P :</b> (510) 555-0142</p>
        <p><b>E :</b> info@42plumova.com</p>
      </div>
      <p class="contact__web">www.42plumova.com</p>
    </div>
  </section>

  <section class="card card--back" aria-label="Card back">
    <p class="brand-name">42 Plumova</p>
  </section>
</body>
</html>
```